https://dorvakel.com

We need a cool technology design for our Managed IT Services company. We are located in Coral Springs Florida. We provide all IT services and support for small to medium sized businesses. We would like to see designs that use our blue and white colors from our website.

```html
<!DOCTYPE html>
<html lang="en">
<head>
<meta charset="utf-8">
<title>Dorvakel Business Card</title>
<link rel="stylesheet" href="https://fonts.googleapis.com/css2?family=Open+Sans:wght@400;700&family=Courier+Prime:wght@400;700&family=Roboto+Condensed:wght@300;400&family=Questrial&display=swap">
<style>
  :root {
    --navy: #1b2b4b;
    --blue: #3a6db0;
    --white: #ffffff;
    --ink: #1c1f26;
    --backdrop: #e9ebee;
  }
  * { margin: 0; padding: 0; box-sizing: border-box; }
  html, body { width: 900px; height: 1200px; overflow: hidden; }
  body { background: var(--backdrop); position: relative; font-family: "Open Sans", sans-serif; }

  .card {
    position: absolute; left: 88px; width: 732px; height: 430px;
    border-radius: 22px; overflow: hidden;
    box-shadow: 0 6px 18px rgba(0,0,0,0.18);
  }
  .card--front { top: 126px; background: var(--white); }
  .card--back { top: 640px; background: var(--navy); }

  .front-art {
    position: absolute; inset: 0;
    background:
      radial-gradient(ellipse 260px 220px at 600px 330px, rgba(79,140,210,0.45), transparent 70%),
      radial-gradient(ellipse 220px 200px at 90px 170px, rgba(170,195,225,0.45), transparent 70%),
      linear-gradient(180deg, #f4f8fc 0%, #ffffff 40%, #eef4fa 100%);
  }
  .front-content { position: absolute; inset: 0; text-align: center; color: var(--ink); }
  .wordmark {
    font-family: "Open Sans", sans-serif; font-weight: 700;
    letter-spacing: -1px; line-height: 1;
  }
  .front-content .wordmark {
    position: absolute; left: 0; right: 0; top: 90px;
    font-size: 50px; color: var(--navy);
  }
  .person-name {
    position: absolute; left: 0; right: 0; top: 174px;
    font-family: "Courier Prime", monospace; font-weight: 700;
    font-size: 24px; letter-spacing: 5px; color: var(--navy);
  }
  .person-title {
    position: absolute; left: 0; right: 0; top: 204px;
    font-family: "Courier Prime", monospace; font-weight: 400;
    font-size: 17px; letter-spacing: 4px; color: var(--blue);
  }
  .contact, .address { font-family: "Questrial", sans-serif; font-size: 17px; }
  .contact { position: absolute; left: 0; right: 0; top: 240px; line-height: 23px; }
  .address { position: absolute; left: 0; right: 0; top: 320px; line-height: 27px; }

  .back-art {
    position: absolute; right: 0; top: 0; width: 400px; height: 100%;
    background:
      radial-gradient(ellipse 200px 160px at 240px 260px, rgba(220,240,255,0.7), transparent 70%),
      linear-gradient(90deg, rgba(27,43,75,1) 0%, rgba(40,110,190,0.85) 30%, #2f8fe0 65%, #1d5fae 100%);
  }
  .back-content .wordmark {
    position: absolute; left: 68px; top: 60px;
    font-size: 44px; color: var(--white);
  }
  .services {
    position: absolute; left: 44px; top: 144px; list-style: none;
    font-family: "Roboto Condensed", sans-serif; font-size: 23px;
    color: var(--white); line-height: 32.2px; text-transform: uppercase;
  }
  .services li { display: flex; align-items: center; }
  .services li::before {
    content: ""; width: 8px; height: 8px; background: var(--white); margin-right: 12px;
  }
  .services b { font-weight: 400; }
  .services span { font-weight: 300; opacity: 0.9; margin-left: 6px; }
</style>
</head>
<body>
  <section class="card card--front">
    <div class="front-art" role="img" aria-label="Soft technology backdrop with faint globe, network nodes and data lines"></div>
    <div class="front-content">
      <div class="wordmark">DORVAKEL</div>
      <div class="person-name">MARLOW TEAGUE-ANSELL</div>
      <div class="person-title">CHIEF EXECUTIVE OFFICER</div>
      <div class="contact">
        <div>(555) 014-2876</div>
        <div>yourname@dorvakel.com</div>
        <div>www.dorvakel.com</div>
      </div>
      <div class="address">
        <div>2870 Palmcrest Blvd #140</div>
        <div>Lindenwood Bay, Floravia 90412</div>
      </div>
    </div>
  </section>

  <section class="card card--back">
    <div class="back-art" role="img" aria-label="Blue digital globe with connected network icons"></div>
    <div class="back-content">
      <div class="wordmark">DORVAKEL</div>
      <ul class="services">
        <li><b>Managed IT</b></li>
        <li><b>IT Data</b><span>Services</span></li>
        <li><b>Security</b><span>Services</span></li>
        <li><b>Software Services</b></li>
        <li><b>Hardware</b><span>Services</span></li>
        <li><b>Business Services</b></li>
        <li><b>Cloud IT</b></li>
        <li><b>Industry Specific</b></li>
      </ul>
    </div>
  </section>
</body>
</html>
```